Business Stationary & Card Design

Double sided business cards, letterhead, horizontal brochure, and envelope design using our logo. We want a modern minimal look. One side of the business card should be only our logo and maybe our slogan "Get It Done Right". The other side should include our coil spring and not the logo again. Watermark like (or not) positioned partially, horizontal, on angle, or a combination of. IF a background color or accent color is used we like blue (4885ed). The letterhead, brochure, and envelope design should be similar to the card. Except no solid background color.Maybe the spring at the bottom of the letterhead page watermark style and partial. Additional info on the business card should be present:
Employee Name
Position
Phone
Email
Address
The final design should communicate strength, simplicity, and newness.

Target Market(s)

35-55 Male & Female

Industry/Entity Type

Automotive

Contact Information for Business Card

One side of the double sided business card should be only our logo and maybe our slogan "Get It Done Right". The other side should include our coil spring and not the logo again. Watermark like (or not) positioned partially, horizontal, on angle, or a combination of. IF a background color or accent color is used we like blue (4885ed). Additional info on the business card should be present:
Employee Name
Position
Phone
Email
Address

Font styles to use
Other font styles liked:
• Use font that compliments the attached font. Maybe plain eurostyle?

Colors
0492cd
3276b5

Requirements
Must have
• Use the coil spring in a subtle unique way (s). Double sided business card
Should not have
• Clutter, colors that do not coordinate well with our logo. Fonts that do not compliment our font.

```html
<!DOCTYPE html>
<html lang="en">
<head>
<meta charset="utf-8">
<title>Ironleaf Motors – Business Card</title>
<link rel="stylesheet" href="https://fonts.googleapis.com/css2?family=Exo+2:wght@400;500;700&display=swap">
<style>
  :root {
    --stage: #2b2b2b;
    --card: #1b1b1b;
    --card-texture: #232323;
    --accent: #e3cf1f;
    --ink: #f2f2f2;
    --ink-soft: #c9c9c9;
    --silver: #dcdcdc;
    --rule: #8e8e8e;
  }
  * { box-sizing: border-box; margin: 0; padding: 0; }
  html, body {
    width: 1200px; height: 1017px; overflow: hidden;
    background: var(--stage);
    font-family: "Exo 2", "Helvetica Neue", Arial, sans-serif;
  }
  .sheet { position: relative; width: 1200px; height: 1017px; }
  .card {
    position: absolute;
    width: 560px; height: 320px;
    background: var(--card);
    box-shadow: 0 24px 50px rgba(0,0,0,.45);
    overflow: hidden;
  }
  .card__texture {
    position: absolute; inset: 0;
    background: repeating-linear-gradient(90deg, var(--card) 0 18px, var(--card-texture) 18px 34px);
    opacity: .55;
  }
  .card--front { left: 80px; top: 130px; }
  .card--back { left: 560px; top: 560px; }

  .brand {
    position: absolute; left: 0; right: 0; top: 112px;
    text-align: center;
    font-weight: 700; font-size: 46px; letter-spacing: 2px;
    color: var(--accent);
    line-height: 1;
  }
  .slogan {
    position: absolute; left: 0; right: 0; top: 196px;
    text-align: center;
    font-weight: 400; font-size: 14px; letter-spacing: .5px;
    color: var(--ink);
  }

  .contact { position: absolute; left: 40px; top: 62px; }
  .contact__name {
    font-weight: 500; font-size: 22px; letter-spacing: .5px;
    color: var(--accent); line-height: 1.1;
  }
  .contact__role {
    font-weight: 500; font-size: 15px; color: var(--ink);
    letter-spacing: .5px; margin-top: 2px;
  }
  .contact__rule {
    width: 200px; height: 2px; background: var(--rule);
    margin: 14px 0 14px;
  }
  .contact__list { list-style: none; }
  .contact__item {
    display: flex; align-items: center; gap: 8px;
    font-size: 14px; color: var(--ink-soft); line-height: 21px;
  }
  .contact__item--plain { padding-left: 20px; }
  .contact__icon { width: 12px; height: 12px; flex: none; }

  .back-mark {
    position: absolute; right: 36px; top: 48px;
    font-weight: 700; font-size: 26px; letter-spacing: 2px;
    color: var(--silver);
  }
</style>
</head>
<body>
<main class="sheet">

  <section class="card card--front" aria-label="Business card front">
    <div class="card__texture" role="img" aria-label="Faint repeated coil spring texture across the card"></div>
    <h1 class="brand">IRONLEAF MOTORS</h1>
    <p class="slogan">Get It Done Right</p>
  </section>

  <section class="card card--back" aria-label="Business card back">
    <div class="card__texture" role="img" aria-label="Faint repeated coil spring texture across the card"></div>
    <div class="back-mark">IRONLEAF</div>

    <div class="contact">
      <h2 class="contact__name">DANIEL REYES</h2>
      <p class="contact__role">CEO/FOUNDER</p>
      <div class="contact__rule"></div>
      <ul class="contact__list">
        <li class="contact__item contact__item--plain">4120 Birchwood Road</li>
        <li class="contact__item contact__item--plain">Fairbanks, Alaska 99701</li>
        <li class="contact__item">
          <svg class="contact__icon" viewBox="0 0 12 12" aria-hidden="true"><path d="M2.5 1h2l1 3-1.3 1a6 6 0 0 0 2.8 2.8l1-1.3 3 1v2a1 1 0 0 1-1 1A9.5 9.5 0 0 1 1.5 2a1 1 0 0 1 1-1z" fill="var(--accent)"/></svg>
          555 214 7390
        </li>
        <li class="contact__item">
          <svg class="contact__icon" viewBox="0 0 12 12" aria-hidden="true"><rect x="0.5" y="2" width="11" height="8" fill="var(--accent)"/><path d="M0.5 2.5 6 6.5l5.5-4" fill="none" stroke="var(--card)" stroke-width="1"/></svg>
          daniel@ironleafmotors.com
        </li>
        <li class="contact__item">
          <svg class="contact__icon" viewBox="0 0 12 12" aria-hidden="true"><circle cx="6" cy="6" r="5.5" fill="var(--accent)"/><path d="M0.5 6h11M6 0.5c-3 3-3 8 0 11M6 0.5c3 3 3 8 0 11" fill="none" stroke="var(--card)" stroke-width=".8"/></svg>
          www.ironleafmotors.com
        </li>
      </ul>
    </div>
  </section>

</main>
</body>
</html>
```